Lumora business card for a plastic surgeon

we need a business card for plastic surgeons that work on a clinic called LUMORA.
we want a clean design and the following informations: name of the doctor, doctor's registration number (called CRM), telephone, address, facebook, instagram.
Colors: white, blue tones, light brown/ coffee

facebook and instagram: lumoraesteticaclinica

Industry/Entity Type

Business

Contact Information for Business Card

clean design

Font styles to use
Serif
Sans Serif
Other font styles liked:
• helvetica light

Colors
cee9f5
85cae6
85abd2
3276b5
cfeae6
cedeed
eaf1f7

Requirements
Must have
• doctor's name
• identification number (called CRM)
• contact (phone, facebook, instagram, address)

```html
<!DOCTYPE html>
<html lang="pt">
<head>
<meta charset="utf-8">
<title>Lumora – Business Card</title>
<link rel="stylesheet" href="https://fonts.googleapis.com/css2?family=Cinzel:wght@400;500&family=EB+Garamond:wght@400;600&display=swap">
<style>
  :root {
    --bg: #2b2b2b;
    --card: #f7f8f9;
    --cyan: #2bb3d0;
    --navy: #14305f;
    --slate: #3d5270;
    --text: #555a60;
    --ink: #1e1e1e;
  }
  * { margin: 0; padding: 0; box-sizing: border-box; }
  html, body { width: 1200px; height: 873px; overflow: hidden; background: var(--bg); }
  .stage { position: relative; width: 1200px; height: 873px; }
  .card {
    position: absolute; width: 560px; height: 320px;
    background: var(--card); overflow: hidden; border-radius: 3px;
    box-shadow: 0 10px 30px rgba(0,0,0,.45);
  }
  .card--front { left: 30px; top: 276px; }
  .card--back { left: 610px; top: 276px; }
  .card__bands { position: absolute; left: 0; bottom: 0; width: 560px; height: 70px; }

  .brand { position: absolute; text-align: center; font-family: "Cinzel", serif; }
  .brand__name { color: var(--cyan); font-weight: 400; letter-spacing: .04em; line-height: 1; display: flex; align-items: center; justify-content: center; gap: .25em; }
  .brand__dot { display: inline-block; width: .28em; height: .28em; border-radius: 50%; background: var(--cyan); }
  .brand__tagline { color: var(--slate); letter-spacing: .08em; line-height: 1.1; margin-top: .15em; }

  .card--front .brand { left: 40px; top: 92px; width: 440px; }
  .card--front .brand__name { font-size: 74px; }
  .card--front .brand__tagline { font-size: 30px; }

  .card--back .brand { left: 180px; top: 38px; width: 260px; }
  .card--back .brand__name { font-size: 42px; }
  .card--back .brand__tagline { font-size: 17px; }

  .doctor { position: absolute; right: 40px; top: 146px; text-align: right; font-family: "EB Garamond", serif; }
  .doctor__name { color: var(--cyan); font-weight: 600; font-size: 18px; }
  .doctor__role { color: var(--ink); font-size: 14px; }
  .doctor__crm { color: var(--text); margin-left: 10px; }

  .contact-tab { position: absolute; left: 0; top: 172px; width: 38px; height: 124px; }
  .contact-list { position: absolute; left: 58px; top: 172px; list-style: none; font-family: "EB Garamond", serif; font-size: 15px; color: var(--text); }
  .contact-list li { height: 31px; line-height: 31px; }
</style>
</head>
<body>
<main class="stage">

  <section class="card card--front" aria-label="Card front">
    <div class="brand">
      <div class="brand__name"><span class="brand__dot"></span>LUMORA</div>
      <div class="brand__tagline">CIRURGIA PLÁSTICA</div>
    </div>
    <svg class="card__bands" viewBox="0 0 560 70" aria-hidden="true">
      <path d="M340 30 Q340 22 352 22 L560 22 L560 56 L340 56 Z" fill="var(--cyan)"/>
      <path d="M0 58 L330 48 Q336 47 340 47 L560 47 L560 70 L0 70 Z" fill="var(--navy)"/>
      <path d="M338 47 Q336 30 352 27" fill="none" stroke="var(--card)" stroke-width="3"/>
    </svg>
  </section>

  <section class="card card--back" aria-label="Card back">
    <div class="brand">
      <div class="brand__name"><span class="brand__dot"></span>LUMORA</div>
      <div class="brand__tagline">CIRURGIA PLÁSTICA</div>
    </div>

    <div class="doctor">
      <div class="doctor__name">Dr Daniel Reyes</div>
      <div class="doctor__role">Plastic Surgeon <span class="doctor__crm">CRM: 528 174 906</span></div>
    </div>

    <svg class="contact-tab" viewBox="0 0 38 124" aria-hidden="true">
      <path d="M0 0 L28 0 Q38 0 38 10 L38 114 Q38 124 28 124 L0 124 Z" fill="var(--cyan)"/>
      <!-- phone -->
      <path d="M12 10 Q11 14 15 19 Q19 23 23 22 L25 19 L21 17 L19 19 Q16 17 15 14 L17 12 L15 8 Z" fill="#fff"/>
      <!-- social placeholders -->
      <circle cx="18" cy="46" r="5" fill="#fff"/>
      <circle cx="18" cy="77" r="5" fill="#fff"/>
      <!-- pin -->
      <path d="M18 100 a6 6 0 0 1 6 6 c0 4-6 10-6 10 s-6-6-6-10 a6 6 0 0 1 6-6z" fill="#fff"/>
      <circle cx="18" cy="106" r="2.2" fill="var(--cyan)"/>
    </svg>
    <ul class="contact-list">
      <li>04150286637</li>
      <li>/lumoraesteticaclinica</li>
      <li>@lumoraesteticaclinica</li>
      <li>82 Harlow Lane Brookfield, PA 15230</li>
    </ul>

    <svg class="card__bands" viewBox="0 0 560 70" aria-hidden="true">
      <path d="M340 30 Q340 22 352 22 L560 22 L560 56 L340 56 Z" fill="var(--cyan)"/>
      <path d="M0 58 L330 48 Q336 47 340 47 L560 47 L560 70 L0 70 Z" fill="var(--navy)"/>
      <path d="M338 47 Q336 30 352 27" fill="none" stroke="var(--card)" stroke-width="3"/>
    </svg>
  </section>

</main>
</body>
</html>
```